Coldmerrow Brochure & Fact Sheet

We need a brochure designed that we will distribute both digitally (PDF) and also have printed. We our an IT company and would like the creative to reflect our brand and industry. All content is written and ready to go. We need each page of the brochure provided as an individual file so we can arrange the pages as needed.

```html
<!DOCTYPE html>
<html lang="en">
<head>
<meta charset="utf-8">
<title>Coldmerrow Brochure Pages</title>
<link href="https://fonts.googleapis.com/css2?family=Oswald:wght@500;600&family=Open+Sans:ital,wght@0,400;0,600;0,700;1,400;1,600&display=swap" rel="stylesheet">
<style>
:root{
  --bg:#d9d9d9;
  --blue:#3f64b9;
  --frame-grey:#8d8f93;
  --ink:#1f1f1f;
  --muted:#555;
  --white:#fff;
  --table-head:#5878c4;
}
*{box-sizing:border-box;margin:0;padding:0}
html,body{width:1200px;height:1200px;overflow:hidden;background:var(--bg)}
body{position:relative;font-family:"Open Sans",Arial,sans-serif;color:var(--ink)}
.page{position:absolute;width:355px;height:459px;box-shadow:0 3px 8px rgba(0,0,0,.22);
  background:linear-gradient(150deg,var(--blue) 0 47%,var(--frame-grey) 47% 100%)}
.sheet{position:absolute;left:14px;top:14px;right:15px;bottom:16px;background:var(--white);overflow:hidden}
.brand{position:absolute;left:0;right:0;display:flex;align-items:center;justify-content:center;gap:6px;
  font-weight:600;font-size:18px;letter-spacing:-.6px;color:var(--ink);z-index:2}
.brand .dot{width:15px;height:15px;border-radius:50%;background:var(--ink)}
.photo{position:absolute;left:0;right:0;top:0;height:179px}
.title-band{position:absolute;left:0;right:0;top:112px;height:67px;background:rgba(255,255,255,.82);text-align:center}
.page-title{font-family:"Oswald",sans-serif;font-weight:600;font-size:17px;color:var(--ink);letter-spacing:-.2px}
.title-band .page-title{margin-top:20px}
.rule{width:30px;height:3px;background:var(--blue);margin:7px auto 0}
.body{position:absolute;left:26px;right:26px;font-size:5.2px;line-height:1.4;color:var(--muted);text-align:center}
.body p{margin-bottom:5px}
.sub{color:var(--blue);font-weight:600;font-size:6.4px;margin:6px 0 4px}
.item-head{font-style:italic;font-weight:600;color:var(--ink);font-size:4.8px;text-transform:uppercase;margin-top:3px}

.about .photo{top:54px;height:125px;background:linear-gradient(180deg,#c9d3df 0%,#8a96a8 45%,#4d5566 100%)}
.about-head{position:absolute;top:186px;left:0;right:0;text-align:center}
.about-head .kicker{font-size:10.5px;font-weight:600;color:var(--muted)}
.about-head .page-title{font-size:21px;margin-top:2px}
.about .lead{font-weight:700;color:var(--ink);font-size:6.3px;margin-bottom:9px}
.about .body{top:248px;left:25px;right:25px;font-size:5.6px;line-height:1.5}
.about .body p{margin-bottom:8px}
.contact{position:absolute;left:25px;right:22px;top:393px;display:flex;gap:14px;font-size:4.6px;color:var(--muted)}
.contact .label{font-family:"Oswald",sans-serif;font-weight:600;font-size:9px;color:var(--ink);line-height:1.2;margin-top:4px;width:58px}
.contact dl{line-height:1.55}
.contact b{color:var(--ink)}

.facts .photo{background:linear-gradient(180deg,#6f86b9 0%,#e7a989 48%,#8f8a99 78%,#c7ccd6 100%)}
.fact-table{position:absolute;left:62px;right:20px;top:195px;font-size:4.9px;line-height:1.45;color:var(--ink)}
.fact-row{display:flex;margin-bottom:6px}
.fact-row dt{width:112px;font-weight:700}
.fact-row dd{flex:1}

.managed .photo{background:linear-gradient(180deg,#d8dde4 0%,#9aa5b3 55%,#6e7684 100%)}
.managed .body{top:194px;left:24px;right:24px;font-size:5.1px;line-height:1.45}
.cols{display:grid;grid-template-columns:1fr 1fr;gap:10px;text-align:center;font-size:5px;line-height:1.5;margin-top:2px}
.col-head{color:var(--blue);font-style:italic;font-size:5px;margin:4px 0 1px}

.strata .photo{background:linear-gradient(160deg,#d9d0c3 0%,#c29c6d 50%,#9c7a55 100%)}
.strata .body{top:196px;left:25px;right:25px;font-size:4.7px}
.strata .tag{color:var(--ink);font-family:"Oswald",sans-serif;font-size:5.6px;text-align:left;margin:6px 0 3px}
.strata .tag span{color:var(--blue)}
.cap-table{width:100%;border-collapse:collapse;font-size:4px;color:var(--ink);text-align:left}
.cap-table th{background:var(--table-head);color:var(--white);text-align:center;font-weight:600;padding:1px;border:1px solid #9aa}
.cap-table td{border:.6px solid #8a8f99;padding:1px 4px;height:8.6px;font-weight:600}

.consult .photo{background:linear-gradient(180deg,#e9ecf1 0%,#b9c1cd 55%,#7d8696 100%)}
.consult .body{top:194px;left:24px;right:24px;font-size:5px;line-height:1.45}
.consult .body p{margin-bottom:2px}

.thanks{background:var(--blue)}
.thanks .photo{height:333px;background:radial-gradient(ellipse at 50% 45%,#6f8fd0 0%,var(--blue) 70%);opacity:.9}
.thanks .brand{top:174px;color:var(--white);font-size:13px;gap:4px}
.thanks .brand .dot{width:10px;height:10px;background:var(--white)}
.thanks .big{position:absolute;top:200px;left:0;right:0;text-align:center;font-family:"Oswald",sans-serif;font-weight:600;font-size:36px;color:var(--white);letter-spacing:.3px}
.thanks .band{position:absolute;left:0;right:0;top:333px;height:94px;background:var(--white)}
.thanks .band .page-title{text-align:center;margin-top:8px;font-size:14px}
.thanks .info{display:flex;justify-content:space-between;padding:9px 38px 0 40px;font-size:4.8px;color:var(--ink);line-height:2}
.ico{display:inline-block;width:5px;height:5px;vertical-align:middle;margin-right:4px}
</style>
</head>
<body>

<section class="page about" style="left:38px;top:120px">
  <div class="sheet">
    <div class="brand" style="top:16px"><span class="dot"></span>coldmerrow</div>
    <div class="photo" role="img" aria-label="City skyline of tall office towers seen from above"></div>
    <div class="about-head">
      <div class="kicker">About Us</div>
      <div class="page-title">Coldmerrow</div>
      <div class="rule"></div>
    </div>
    <div class="body">
      <p class="lead">Harness the Potential of Technology with Coldmerrow</p>
      <p>We believe technology can turn good businesses into industry leaders, but it is never a sure thing. Tools alone will not produce results. It takes experience, solid planning and honest advice built on your own background, shaped by your goals and ready to put into action.</p>
      <p>It is when you pair a strong platform with clear ideas and tailored IT strategies that real results follow. <b style="color:#1f1f1f">And that's why we're here.</b></p>
      <p>At Coldmerrow, our team is known for being inventive, proactive and easy to work with. We treat customers as partners and advisors in the process, and rather than rushing ahead without thought, we move with care, making every step grounded in understanding, clarity and enablement. In the end, we want you to leave with a personal set of IT strategies you <b style="color:#1f1f1f">understand, value, and feel empowered to implement.</b></p>
    </div>
    <div class="contact">
      <div class="label">Contact<br>Coldmerrow</div>
      <dl>
        <div><svg class="ico" viewBox="0 0 10 10"><circle cx="5" cy="4" r="3" fill="#3f64b9"/></svg>418 Harbor Lane NW, Alder Falls,<br>&nbsp;&nbsp;&nbsp;&nbsp;&nbsp;MI 49001</div>
        <div>&nbsp;&nbsp;&nbsp;&nbsp;&nbsp;www.coldmerrow.example</div>
        <div>&nbsp;&nbsp;&nbsp;&nbsp;&nbsp;1.800.555-0142</div>
      </dl>
      <dl>
        <div><b>Email</b></div>
        <div><i>General Questions:</i> info@coldmerrow.example</div>
        <div><i>Sales:</i> sales@coldmerrow.example</div>
        <div><i>Careers:</i> careers@coldmerrow.example</div>
      </dl>
    </div>
  </div>
</section>

<section class="page facts" style="left:424px;top:120px">
  <div class="sheet">
    <div class="photo" role="img" aria-label="Downtown skyline at sunset"></div>
    <div class="brand" style="top:16px"><span class="dot"></span>coldmerrow</div>
    <div class="title-band"><div class="page-title">Coldmerrow Facts</div><div class="rule"></div></div>
    <dl class="fact-table">
      <div class="fact-row"><dt>Established</dt><dd>2000</dd></div>
      <div class="fact-row"><dt>Headquarters</dt><dd>418 Harbor Lane NW<br>Alder Falls, MI 49001</dd></div>
      <div class="fact-row"><dt>Executive Leadership</dt><dd>Dana Whitcombe, CEO<br>Ross Kellerman, COO<br>Alan Pryce, VP Digital Transformation<br>Tessa Marlow, VP Sales &amp; Marketing</dd></div>
      <div class="fact-row"><dt>Team Members</dt><dd>25</dd></div>
      <div class="fact-row"><dt>Combined Staff Experience</dt><dd>85+ Years</dd></div>
      <div class="fact-row"><dt>Core Services</dt><dd>Full Service Managed IT Services<br>Stratafield Website Development<br>IT Consulting</dd></div>
      <div class="fact-row"><dt>Accolades</dt><dd>Lakeshore 100 Top Workplaces<br>Managed Provider 500<br>Stratafield Website of the Year 2013<br>Stratafield Website of the Year 2014<br>Stratafield Website of the Year 2015<br>Stratafield Website of the Year 2017<br>Stratafield Partner of the Year 2016</dd></div>
      <div class="fact-row"><dt>Certifications</dt><dd>Stratafield Elite Partner<br>Northgate Certified Gold Partner<br>Virtano Certified Partner<br>Storalyn Certified Partner<br>Backvault Certified Partner<br>Wallkeep Certified Partner</dd></div>
    </dl>
  </div>
</section>

<section class="page managed" style="left:810px;top:120px">
  <div class="sheet">
    <div class="photo" role="img" aria-label="Two businessmen looking at a laptop together"></div>
    <div class="brand" style="top:16px"><span class="dot"></span>coldmerrow</div>
    <div class="title-band"><div class="page-title">Coldmerrow Managed IT Services</div><div class="rule"></div></div>
    <div class="body">
      <p>Managed Services by Coldmerrow deliver proactive monitoring, upkeep, security and IT support for small and medium businesses, covering infrastructure, applications and cloud solutions. Based in the Lakeshore region, we offer a hands-on approach and complete IT solutions that help your company grow, stay efficient and keep a lean IT operation. Our dedicated infrastructure team keeps your business running smoothly with no downtime, around the clock. IT should not be a distraction, it should be a tool, and that is our job.</p>
      <div class="sub">Our Managed IT Services Approach</div>
      <div class="cols">
        <div>
          <div class="col-head">Infrastructure</div>
          <p>We focus on designing a streamlined IT system that runs in harmony and improves workflow. We manage, monitor and maintain every network and server on your premises or remotely, with round-the-clock monitoring that lets us respond fast, avoid downtime and spot bottlenecks early. When it comes to IT, we stay on top of things so you don't have to.</p>
          <div class="col-head">Security</div>
          <p>Our security services include endpoint protection, network security, cloud security and policy management. We protect partners from modern threats by helping them outline, apply and maintain custom security policies, and we keep everyone informed on how to protect their business.</p>
          <div class="col-head">Customer service is at the core of our team</div>
          <p>Our Managed IT Services succeed because a dedicated, experienced team makes sure staff get quick answers and expert support they can trust.</p>
        </div>
        <div>
          <div class="col-head">Disaster Recovery</div>
          <p>However well protected you are, it pays to plan for the unexpected. We work with partners to plan, deliver and manage recovery solutions that fit their IT needs, including offsite backups and redundant systems. Be proactive and have your plan B ready.</p>
          <div class="col-head">Desktop Management</div>
          <p>We help your staff focus on daily business by keeping workstations current and fielding support questions at any hour. Count on reliable and secure workspaces from Coldmerrow.</p>
          <div class="col-head">Cloud Management</div>
          <p>Valuable business data must be stored and protected. We help you choose the best model, whether cloud, onsite or a hybrid, and assist with setup, monitoring and upkeep.</p>
        </div>
      </div>
    </div>
  </div>
</section>

<section class="page strata" style="left:38px;top:608px">
  <div class="sheet">
    <div class="photo" role="img" aria-label="Hands typing on a laptop beside printed documents on a desk"></div>
    <div class="brand" style="top:16px"><span class="dot"></span>coldmerrow</div>
    <div class="title-band"><div class="page-title">Coldmerrow Stratafield Development</div><div class="rule"></div></div>
    <div class="body">
      <p>As a Premier Partner of Stratafield, we build dynamic content management systems that work across the enterprise, giving you the ability and insight to reach your customers. Our experience covers content personalization, multilingual support, digital marketing, workflow and hosting for small to medium businesses.</p>
      <p>Four-time Stratafield Website of the Year recipient, Coldmerrow has a record of helping clients become leaders in their industry.</p>
      <p>We know today's customers expect personal website experiences and timely content. Those expectations push us to align systems, processes and people in a way that creates meaningful experiences.</p>
      <p>We believe Stratafield has mastered the online user experience, and we have given our people the depth to become experts in the platform.</p>
      <p>"We take the time to help companies find the best platform to reach their growth goals. Time and again, Stratafield proves to be the right fit for many of our clients." Alan Pryce, VP of Architecture.</p>
      <p class="sub" style="font-size:5px">Turn problems into answers with Coldmerrow.</p>
      <p>Our staff work to learn what success means to you, then together we decide how best to clear the obstacles in the way. From large firms to regional leaders, we build long-term relationships that lead to lasting IT solutions.</p>
      <div class="tag">Solid Understanding · Sound Strategy · <span>Deliberate Execution</span></div>
      <table class="cap-table">
        <tr><th>Stratafield Capabilities</th><th>Development Tools &amp; Experience</th></tr>
        <tr><td>Stratafield Elite Partner</td><td>Stratafield CMS</td></tr>
        <tr><td>7+ Certified CMS Developers</td><td>WebCore Web API</td></tr>
        <tr><td>Backend Development Specialists</td><td>WebCore MVC</td></tr>
        <tr><td>10+ Certified Framework Developers</td><td>DataBridge Mapper</td></tr>
        <tr><td>Network of partners for strategy, creative and hosting</td><td>ERPline Integration</td></tr>
        <tr><td>2013, 2014, 2015, 2017 Stratafield Site of the Year Winner</td><td>TeamPort</td></tr>
        <tr><td></td><td>Northgate Cloudreach</td></tr>
        <tr><td></td><td>Skyrack Cloud</td></tr>
      </table>
    </div>
  </div>
</section>

<section class="page consult" style="left:424px;top:608px">
  <div class="sheet">
    <div class="photo" role="img" aria-label="Smiling businesswoman in an office with colleagues in a meeting behind her"></div>
    <div class="brand" style="top:16px"><span class="dot"></span>coldmerrow</div>
    <div class="title-band"><div class="page-title">General IT Consulting</div><div class="rule"></div></div>
    <div class="body">
      <p>Beyond Managed IT Services and Stratafield Development, Coldmerrow offers a range of technology solutions and a custom plan of action. With a tailored approach, we help businesses stay competitive, get ahead and remain there.</p>
      <div class="sub">Our Specialties</div>
      <div class="item-head">Virtual CIO Services</div>
      <p>We provide senior leadership that acts as a CIO and IT advisor to your business, helping it run efficiently without a full-time hire.</p>
      <div class="item-head">Vulnerability Management &amp; Patching</div>
      <p>We keep regular network scanning, firewall logging and automated testing in place so weaknesses are found and patched on schedule.</p>
      <div class="item-head">Project Management</div>
      <p>We manage budget, schedule and scope of any IT project, knowing that success depends on people and the process to design and test together.</p>
      <div class="item-head">Solution Architecture</div>
      <p>A disconnected stack never reaches its potential. We align systems and workflows to share data, raise efficiency and improve experiences.</p>
      <div class="item-head">Application Support Services</div>
      <p>Sometimes a ready product does not fit. Our developers use many technologies to support your IT systems and adapt to your needs.</p>
      <div class="item-head">Staff Augmentation</div>
      <p>As part of an outsourcing strategy, we provide complete staff augmentation and recruiting for clients that value their HR investments.</p>
      <p style="margin-top:4px">Whatever the client or project, we meet every challenge with an integrated process based on insight, clarity and enablement. Contact us today to learn more about our problem solving and IT architecture; we are here to help you use technology to your advantage, now and in the future.</p>
    </div>
  </div>
</section>

<section class="page thanks" style="left:810px;top:608px">
  <div class="photo" role="img" aria-label="Faint blue-tinted photo of a smiling businesswoman with colleagues"></div>
  <div class="brand"><span class="dot"></span>coldmerrow</div>
  <div class="big">THANK YOU</div>
  <div class="band">
    <div class="page-title">Coldmerrow</div>
    <div class="info">
      <div>
        <div><svg class="ico" viewBox="0 0 10 10"><path d="M5 1a3 3 0 0 1 3 3c0 2-3 5-3 5S2 6 2 4a3 3 0 0 1 3-3z" fill="#3f64b9"/></svg>418 Harbor Lane NW, Alder<br>&nbsp;&nbsp;&nbsp;&nbsp;&nbsp;&nbsp;Falls, MI 49001</div>
        <div><svg class="ico" viewBox="0 0 10 10"><circle cx="5" cy="5" r="3.5" fill="none" stroke="#3f64b9"/></svg>www.coldmerrow.example</div>
        <div><svg class="ico" viewBox="0 0 10 10"><rect x="3" y="1" width="4" height="8" rx="1" fill="#3f64b9"/></svg>1.800.555-0142</div>
      </div>
      <div style="line-height:1.8">
        <div><svg class="ico" viewBox="0 0 10 10"><rect x="1" y="2.5" width="8" height="5" fill="#3f64b9"/></svg><b>Email</b></div>
        <div><i>General Questions:</i> info@coldmerrow.example</div>
        <div><i>Sales:</i> sales@coldmerrow.example</div>
        <div><i>Careers:</i> careers@coldmerrow.example</div>
      </div>
      <div>
        <div><svg class="ico" viewBox="0 0 10 10"><circle cx="5" cy="5" r="4" fill="#3f64b9"/></svg>/coldmerrow</div>
        <div><svg class="ico" viewBox="0 0 10 10"><circle cx="5" cy="5" r="4" fill="#3f64b9"/></svg>/coldmerrow</div>
        <div><svg class="ico" viewBox="0 0 10 10"><circle cx="5" cy="5" r="4" fill="#3f64b9"/></svg>/company/coldmerrow</div>
      </div>
    </div>
  </div>
</section>

</body>
</html>
```